Logistics Website Design

See website https://tvarfreightglobal.com for theme and color details. Need the site to be re-done and reflect some of the designs shown in this list here: https://pinvora.com/tags/logistics-company-website

Target Market(s)

Logistics & Transportation

Industry/Entity Type

Logistics and Supply Chain

Coding

Coded - Design and coding required

Number of Pages Required

5+ page

Requirements
Must have
• Colors must match theme of logo. Looking for a sleek, interactive design.

```html
<!DOCTYPE html>
<html lang="en">
<head>
<meta charset="utf-8">
<title>Tvar Freight Global — Logistics</title>
<link href="https://fonts.googleapis.com/css2?family=Bebas+Neue&family=Outfit:wght@400;500;600&display=swap" rel="stylesheet">
<style>
:root{
  --bg:#140504;
  --bg-story:#1f0c09;
  --bg-footer:#0f0302;
  --orange:#fb6a3a;
  --orange-deep:#e5532a;
  --white:#ffffff;
  --muted:#e8dcd8;
  --field:#f1f0f0;
  --field-text:#6b6363;
  --panel:#1e0b08;
}
*{box-sizing:border-box;margin:0;padding:0}
html,body{width:1200px;height:3226px;overflow:hidden;background:var(--bg)}
body{font-family:"Outfit",sans-serif;color:var(--white);position:relative}
.abs{position:absolute}
.display{font-family:"Bebas Neue",sans-serif;font-weight:400;letter-spacing:.5px;line-height:1}
.btn{position:absolute;background:var(--orange);color:var(--white);font-size:11px;font-weight:600;text-transform:uppercase;display:flex;align-items:center;justify-content:center;border-radius:6px;letter-spacing:.2px}

/* nav */
.site-header{left:0;top:0;width:1200px;height:78px;background:var(--bg)}
.brand{left:113px;top:14px;display:flex;align-items:center;gap:10px;font-size:18px;font-weight:600}
.brand-dot{width:40px;height:40px;border-radius:50%;background:var(--orange)}
.nav{left:500px;top:0;height:78px;display:flex;align-items:center;gap:42px;font-size:11px;font-weight:500;text-transform:uppercase}
.nav-contact{left:960px;top:16px;width:127px;height:44px}

/* hero */
.hero{left:0;top:78px;width:1200px;height:625px;background:
  linear-gradient(90deg,rgba(20,5,4,.35) 0%,rgba(20,5,4,0) 55%),
  linear-gradient(180deg,#4a1f14 0%,#b04a1e 22%,#e07a2c 36%,#8a3a1c 52%,#3a1a12 70%,#2a1a16 100%)}
.hero-truck{left:600px;top:80px;width:600px;height:470px;border-radius:8px;background:linear-gradient(160deg,#c4552a 0%,#7a2e18 45%,#8f8a88 70%,#5a5250 100%);opacity:.85}
.hero-title{left:113px;top:250px;font-size:64px;width:520px}
.hero-sub{left:113px;top:440px;font-family:"Bebas Neue",sans-serif;font-size:19px}
.hero-cta{left:113px;top:482px;width:160px;height:44px}
.slider{left:510px;top:654px;display:flex;align-items:center;gap:10px;font-size:14px}
.slider .line{width:30px;height:1px;background:var(--white)}

/* marquee */
.ticker{left:0;top:703px;width:1200px;height:111px;display:flex;align-items:center;gap:28px;white-space:nowrap;padding-left:5px}
.ticker span{font-family:"Bebas Neue",sans-serif;font-size:46px;color:transparent;-webkit-text-stroke:1.2px #e6dcd8;letter-spacing:1px}
.ticker i{width:30px;height:30px;border-radius:50%;background:var(--orange);display:inline-block;opacity:.85}

/* intro */
.intro-img{left:163px;top:863px;width:413px;height:256px;border-radius:16px;background:linear-gradient(180deg,#7fb8c9 0%,#c6d6e0 35%,#2a5f86 60%,#0d3b5a 100%)}
.intro-title{left:622px;top:889px;font-size:45px}
.intro-text{left:622px;top:986px;width:420px;font-size:13px;line-height:18.8px;color:var(--muted)}

/* services */
.services-title{left:0;top:1208px;width:1200px;text-align:center;font-size:45px}
.card{position:absolute;top:1270px;width:282px;height:305px}
.card-img{position:absolute;left:0;top:0;width:282px;height:252px;border-radius:14px}
.card-panel{position:absolute;left:24px;top:213px;width:258px;height:92px;background:var(--panel);border-radius:12px;padding:30px 0 0 28px;font-size:22px;line-height:1.05}
.card-icon{position:absolute;right:0;top:189px;width:66px;height:46px;background:var(--orange);border-radius:8px 0 0 0;display:flex;align-items:center;justify-content:center}
.card-arrow{position:absolute;right:15px;top:37px;width:32px;height:32px;border-radius:6px;background:#3a2420;display:flex;align-items:center;justify-content:center}
.view-more{left:517px;top:1613px;width:167px;height:44px}

/* story */
.story{left:0;top:1747px;width:1200px;height:560px;background:var(--bg-story)}
.story-title{left:123px;top:1851px;font-size:42px}
.story-text{left:123px;top:1904px;width:425px;font-size:13px;line-height:18.8px;color:var(--muted)}
.story-text p+p{margin-top:14px}
.story-cta{left:123px;top:2163px;width:122px;height:44px}
.story-img{left:651px;top:1818px;width:425px;height:420px;border-radius:18px;background:linear-gradient(170deg,#6d95b5 0%,#b89d6a 30%,#7a6a4a 50%,#c0562a 62%,#5a5552 80%,#3c3a3a 100%)}

/* contact */
.contact-title{left:0;top:2395px;width:1200px;text-align:center;font-size:44px}
.contact-sub{left:0;top:2447px;width:1200px;text-align:center;font-size:13px;color:var(--muted)}
.field{position:absolute;background:var(--field);border-radius:6px;color:var(--field-text);font-size:11px;text-transform:uppercase;display:flex;align-items:center;gap:10px;padding-left:16px}
.field svg{flex:none}
.field-msg{align-items:flex-start;padding-top:14px}
.submit{left:297px;top:2697px;width:605px;height:45px;border-radius:8px}
.submit svg{position:absolute;right:22px;top:14px}

/* footer */
.site-footer{left:0;top:2837px;width:1200px;height:389px;background:var(--bg-footer)}
.footer-brand{left:0;top:2960px;width:1200px;display:flex;justify-content:center;align-items:center;gap:14px;font-size:28px;font-weight:600}
.footer-brand .brand-dot{width:56px;height:56px}
.footer-nav{left:0;top:3104px;width:1200px;display:flex;justify-content:center;gap:50px;font-size:13px;text-transform:uppercase}
.footer-rule{left:113px;top:3172px;width:974px;height:1px;background:#4a3430}
.copyright{left:0;top:3191px;width:1200px;text-align:center;font-size:12px;color:var(--muted)}
.chat{left:1105px;top:3135px;width:73px;height:73px;border-radius:50%;background:#2e2220;display:flex;align-items:center;justify-content:center}
</style>
</head>
<body>

<header class="abs site-header">
  <div class="abs brand"><span class="brand-dot"></span>Tvar Freight Global</div>
  <nav class="abs nav">
    <svg width="14" height="13" viewBox="0 0 14 13"><path d="M7 0L0 6h2v7h4V9h2v4h4V6h2z" fill="#fb6a3a"/></svg>
    <span>Services</span><span>Industries</span><span>Request a Quote</span><span>About Us</span>
  </nav>
  <div class="btn nav-contact">Contact Us</div>
</header>

<section class="abs hero" role="img" aria-label="Orange semi truck driving on a highway at sunset with mountains behind"></section>
<div class="abs hero-truck" role="img" aria-label="Orange cab truck with silver trailer"></div>
<h1 class="abs display hero-title">Delivering strength in every mile secure</h1>
<p class="abs hero-sub">And reliable transportation for all your cargo needs.</p>
<div class="btn hero-cta">Request a Quote</div>
<div class="abs slider">
  <svg width="10" height="12" viewBox="0 0 10 12"><path d="M7 1L2 6l5 5" stroke="#fff" stroke-width="2" fill="none"/></svg>
  <span>01</span><span class="line"></span><span>02</span><span class="line"></span><span>03</span>
  <svg width="10" height="12" viewBox="0 0 10 12"><path d="M3 1l5 5-5 5" stroke="#fff" stroke-width="2" fill="none"/></svg>
</div>

<div class="abs ticker">
  <span>Supply Chain</span><i></i><span>Warehousing</span><i></i><span>Global Shipping</span><i></i><span>Fast Delivery</span>
</div>

<div class="abs intro-img" role="img" aria-label="Container ship loaded with cargo sailing on open sea"></div>
<h2 class="abs display intro-title">Keeping your<br>supply chain moving</h2>
<p class="abs intro-text">We deliver a comprehensive range of open-deck and specialized transportation services—including flatbed, step deck, heavy haul, and over-dimensional freight solutions. Backed by years of experience, a trusted nationwide carrier network, and a strong safety-first culture, we provide reliable, adaptable logistics support built around the unique requirements of every load.</p>

<h2 class="abs display services-title">Our Services</h2>

<article class="card" style="left:157px">
  <div class="card-img" role="img" aria-label="Worker in safety vest checking a tablet beside a truck" style="background:linear-gradient(135deg,#6a5a55,#b8662f 60%,#9fbf3a)"></div>
  <div class="card-panel display">Flatbed<br>Transportation
    <div class="card-arrow"><svg width="12" height="12" viewBox="0 0 12 12"><path d="M2 10L10 2M4 2h6v6" stroke="#fff" stroke-width="1.4" fill="none"/></svg></div>
  </div>
  <div class="card-icon"><svg width="34" height="24" viewBox="0 0 34 24" fill="none" stroke="#fff" stroke-width="1.8"><rect x="1" y="2" width="20" height="15" rx="2"/><path d="M21 7h7l5 6v4H21z"/><circle cx="8" cy="20" r="3"/><circle cx="26" cy="20" r="3"/></svg></div>
</article>

<article class="card" style="left:459px">
  <div class="card-img" role="img" aria-label="Courier in blue uniform walking between shipping containers" style="background:linear-gradient(135deg,#55606a,#9aa3a8 50%,#2e5e9e)"></div>
  <div class="card-panel display">Step Deck<br>Transportation
    <div class="card-arrow"><svg width="12" height="12" viewBox="0 0 12 12"><path d="M2 10L10 2M4 2h6v6" stroke="#fff" stroke-width="1.4" fill="none"/></svg></div>
  </div>
  <div class="card-icon"><svg width="34" height="24" viewBox="0 0 34 24" fill="none" stroke="#fff" stroke-width="1.8"><path d="M2 14l30-4c1 0 1 3 0 3L6 16zM12 12L8 3h4l8 8M14 15l-2 7h4l6-8"/></svg></div>
</article>

<article class="card" style="left:761px">
  <div class="card-img" role="img" aria-label="Dispatcher in red jacket with clipboard beside a white truck" style="background:linear-gradient(135deg,#8fb0d0,#dcdfe2 45%,#c2302a 75%,#3a5a8a)"></div>
  <div class="card-panel display">Dry Van<br>Transportation
    <div class="card-arrow"><svg width="12" height="12" viewBox="0 0 12 12"><path d="M2 10L10 2M4 2h6v6" stroke="#fff" stroke-width="1.4" fill="none"/></svg></div>
  </div>
  <div class="card-icon"><svg width="34" height="24" viewBox="0 0 34 24" fill="none" stroke="#fff" stroke-width="1.8"><rect x="1" y="3" width="22" height="14" rx="2"/><path d="M23 8h6l4 5v4H23z"/><circle cx="8" cy="20" r="3"/><circle cx="27" cy="20" r="3"/></svg></div>
</article>

<div class="btn view-more">View More Service</div>

<section class="abs story"></section>
<h2 class="abs display story-title">Our Story</h2>
<div class="abs story-text">
  <p>Tvar Freight Global was born out of real-world experience in the fitness equipment industry. What started as a company shipping strength equipment, cardio machines, and training gear to gyms, schools, and commercial facilities quickly evolved into something bigger. As order volume grew and supply chains became more complex, the team developed deep expertise in coordinating freight, managing deliveries, and navigating the challenges of large-scale equipment transportation. That hands-on experience laid the foundation for what would eventually become a full-service logistics operation.</p>
  <p>Recognizing the opportunity to build a more efficient &amp; reliable transportation network, Tvar Freight expanded beyond fitness equipment and began offering logistics.</p>
</div>
<div class="btn story-cta">Read More</div>
<div class="abs story-img" role="img" aria-label="Orange truck on a sunlit road past a rocky hillside"></div>

<h2 class="abs display contact-title">Let's move your business forward</h2>
<p class="abs contact-sub">Let's discuss your logistics needs and how we can help your business thrive</p>

<div class="field" style="left:297px;top:2493px;width:298px;height:41px"><svg width="10" height="10" viewBox="0 0 10 10"><circle cx="5" cy="3" r="2.5" fill="#444"/><path d="M0 10c0-3 2-4.5 5-4.5s5 1.5 5 4.5z" fill="#444"/></svg>First Name</div>
<div class="field" style="left:604px;top:2493px;width:298px;height:41px"><svg width="10" height="10" viewBox="0 0 10 10"><circle cx="5" cy="3" r="2.5" fill="#444"/><path d="M0 10c0-3 2-4.5 5-4.5s5 1.5 5 4.5z" fill="#444"/></svg>Last Name</div>
<div class="field" style="left:297px;top:2543px;width:298px;height:41px"><svg width="11" height="9" viewBox="0 0 11 9"><rect width="11" height="9" rx="1" fill="#444"/><path d="M0 1l5.5 4L11 1" stroke="#f1f0f0" fill="none"/></svg>Email</div>
<div class="field" style="left:604px;top:2543px;width:298px;height:41px"><svg width="10" height="10" viewBox="0 0 10 10"><path d="M2 0l2 2.5-1.2 1.5c.8 1.5 1.7 2.4 3.2 3.2L7.5 6 10 8 8.5 10C4 9.5.5 6 0 1.5z" fill="#444"/></svg>Phone Number</div>
<div class="field field-msg" style="left:297px;top:2593px;width:605px;height:90px"><svg width="11" height="10" viewBox="0 0 11 10"><path d="M5.5 0C8.5 0 11 2 11 4.5S8.5 9 5.5 9L2 10l1-2C1 7 0 6 0 4.5 0 2 2.5 0 5.5 0z" fill="#444"/></svg>Message</div>
<div class="btn submit">Submit Now<svg width="16" height="16" viewBox="0 0 16 16"><path d="M15 1L1 7l5 2 2 5z" fill="#fff"/></svg></div>

<footer class="abs site-footer"></footer>
<div class="abs footer-brand"><span class="brand-dot"></span>Tvar Freight Global</div>
<nav class="abs footer-nav"><span>Home</span><span>Services</span><span>Industries</span><span>Request a Quote</span><span>About Us</span><span>Contact Us</span></nav>
<div class="abs footer-rule"></div>
<p class="abs copyright">© 2026. An independent agent of Halden Ridge LLC.</p>
<div class="abs chat"><svg width="36" height="30" viewBox="0 0 36 30"><path d="M18 2c9 0 16 5 16 12s-7 12-16 12c-2 0-4 0-6-1l-7 4 2-6C4 20 2 17 2 14 2 7 9 2 18 2z" fill="#fb6a3a"/><circle cx="11" cy="14" r="2.2" fill="#fff"/><circle cx="18" cy="14" r="2.2" fill="#fff"/><circle cx="25" cy="14" r="2.2" fill="#fff"/></svg></div>

</body>
</html>
```